Business Card Design

We sell fish products to corporate food companies who then turn these products into final food products for consumers

Industry/Entity Type

Business

Contact Information for Business Card

I need a corporate business card template for a fish products business. We would like it be professional for use in dealing with multi national companies. This company business card template will be used by multiple employees so the following fields must be open to edit (Name, Phone Number and Email address)

```html
<!DOCTYPE html>
<html lang="en">
<head>
<meta charset="utf-8">
<title>Tidewater Fisheries – Business Card</title>
<link href="https://fonts.googleapis.com/css2?family=Open+Sans:wght@400;600;700&display=swap" rel="stylesheet">
<style>
  :root {
    --page-bg: #ecebe8;
    --card-white: #ffffff;
    --panel-light: #e4e4e4;
    --panel-dark: #c9c9c9;
    --brand-blue: #1565c0;
    --accent-bar: #1a5fc4;
    --text-dark: #1c1c1c;
    --icon-dark: #222222;
  }
  html, body {
    margin: 0;
    width: 1200px;
    height: 800px;
    overflow: hidden;
    background: var(--page-bg);
    font-family: "Open Sans", sans-serif;
  }
  .canvas {
    width: 1200px;
    height: 800px;
    display: flex;
    align-items: center;
    justify-content: center;
  }
  .business-card {
    position: relative;
    width: 840px;
    height: 480px;
    border-radius: 14px;
    overflow: hidden;
    display: flex;
    background: var(--card-white);
    box-shadow: 0 6px 22px rgba(0, 0, 0, 0.12);
  }
  .brand-side {
    width: 400px;
    display: flex;
    flex-direction: column;
    align-items: center;
    justify-content: center;
    gap: 18px;
    padding-top: 10px;
  }
  .brand-mark {
    width: 64px;
    height: 64px;
    border-radius: 50%;
    background: var(--brand-blue);
  }
  .brand-name {
    margin: 0;
    color: var(--brand-blue);
    font-weight: 600;
    font-size: 38px;
    line-height: 1.15;
    letter-spacing: 1px;
    text-align: center;
    text-transform: uppercase;
  }
  .contact-side {
    position: relative;
    flex: 1;
    background: linear-gradient(90deg, var(--panel-light) 0%, var(--panel-dark) 100%);
  }
  .contact-side::before {
    content: "";
    position: absolute;
    left: -38px;
    top: 90px;
    border-style: solid;
    border-width: 30px 38px 30px 0;
    border-color: transparent var(--panel-light) transparent transparent;
  }
  .person-name {
    position: absolute;
    left: 56px;
    top: 96px;
    margin: 0;
    font-size: 33px;
    font-weight: 400;
    color: var(--text-dark);
  }
  .person-name .surname { font-weight: 700; }
  .contact-list {
    position: absolute;
    left: 56px;
    top: 240px;
    margin: 0;
    padding: 0;
    list-style: none;
    display: flex;
    flex-direction: column;
    gap: 18px;
  }
  .contact-item {
    display: flex;
    align-items: center;
    gap: 22px;
    font-size: 23px;
    color: var(--text-dark);
  }
  .contact-icon { width: 28px; height: 28px; flex: none; }
  .accent-bar {
    position: absolute;
    left: 0;
    right: 0;
    bottom: 0;
    height: 38px;
    background: var(--accent-bar);
  }
</style>
</head>
<body>
<main class="canvas">
  <article class="business-card">
    <section class="brand-side">
      <span class="brand-mark" aria-hidden="true"></span>
      <h1 class="brand-name">Tidewater<br>Fisheries</h1>
    </section>
    <section class="contact-side">
      <h2 class="person-name">Daniel <span class="surname">Reyes</span></h2>
      <ul class="contact-list">
        <li class="contact-item">
          <svg class="contact-icon" viewBox="0 0 28 28" aria-hidden="true">
            <rect x="1" y="1" width="26" height="26" rx="3" fill="var(--icon-dark)"/>
            <path d="M6 11c0-3 3-4 8-4s8 1 8 4v1h-4v-2h-8v2H6z" fill="#fff"/>
            <rect x="8" y="13" width="12" height="9" rx="1.5" fill="#fff"/>
            <circle cx="14" cy="17.5" r="2" fill="var(--icon-dark)"/>
          </svg>
          <span class="contact-phone">987-654-321</span>
        </li>
        <li class="contact-item">
          <svg class="contact-icon" viewBox="0 0 28 28" aria-hidden="true">
            <rect x="1" y="1" width="26" height="26" rx="3" fill="var(--icon-dark)"/>
            <rect x="5" y="8" width="18" height="12" fill="#fff"/>
            <path d="M5 8l9 7 9-7M5 20l7-6M23 20l-7-6" fill="none" stroke="var(--icon-dark)" stroke-width="1.5"/>
          </svg>
          <span class="contact-email">daniel@tidewater.com</span>
        </li>
      </ul>
      <div class="accent-bar"></div>
    </section>
  </article>
</main>
</body>
</html>
```